Real estate Agent postcards for homeowners

I need a "Just Sold" postcard for two real agents , I am providing pictures of the agents and neighborhood.
I have the front and back of a postcard containing the information I want on the postcard.
I want a designer to take the info and pictures and design a new postcard and choose the colors

Target Market(s)

homeowners of luxury condos

Industry/Entity Type

Real Estate Agent

Colors

Designer to choose colors to be used in the design.

```html
<!DOCTYPE html>
<html lang="en">
<head>
<meta charset="utf-8">
<title>Harborline Realty – Just Sold Postcard</title>
<link rel="stylesheet" href="https://fonts.googleapis.com/css2?family=Oswald:wght@500;600;700&family=Lato:wght@400;700&display=swap">
<style>
  :root {
    --navy: #243a4f;
    --lime: #dde21e;
    --lime-text: #c8cf10;
    --red: #f0201c;
    --ink: #1f2a33;
    --white: #ffffff;
    --stamp: #d6d6d6;
    --rule: #9a9a9a;
  }
  * { box-sizing: border-box; margin: 0; padding: 0; }
  html, body { width: 1200px; height: 1200px; overflow: hidden; background: var(--white); }
  .stage { position: relative; width: 1500px; height: 1500px; transform: scale(0.8); transform-origin: 0 0; }
  .card {
    position: absolute; left: 274px; width: 927px; height: 660px;
    background: var(--white); overflow: hidden;
    box-shadow: 3px 4px 8px rgba(0,0,0,.35);
    font-family: 'Lato', sans-serif; color: var(--ink);
  }
  .card--front { top: 53px; }
  .card--back { top: 773px; height: 662px; }
  .card-art { position: absolute; inset: 0; width: 100%; height: 100%; }
  .abs { position: absolute; }
  .display { font-family: 'Oswald', sans-serif; text-transform: uppercase; }

  .brand-mark { display: flex; align-items: center; gap: 10px; color: var(--white); font-family: 'Oswald', sans-serif; font-weight: 600; font-size: 26px; white-space: nowrap; }
  .brand-mark .square { width: 34px; height: 34px; background: var(--white); }
  .brand-mark--front { left: 46px; top: 34px; }
  .brand-mark--back { left: 466px; top: 34px; color: var(--navy); font-size: 20px; gap: 8px; }
  .brand-mark--back .square { width: 28px; height: 28px; background: var(--navy); }

  .headline { right: 22px; top: 38px; font-size: 94px; font-weight: 700; color: var(--red); line-height: 1; white-space: nowrap; }
  .agency-title { right: 22px; top: 148px; font-size: 52px; font-weight: 600; color: var(--navy); line-height: 1; white-space: nowrap; }
  .listing { right: 32px; text-align: right; font-size: 18px; line-height: 22px; white-space: nowrap; }
  .listing--one { top: 237px; }
  .listing--two { top: 302px; }
  .callout { left: 462px; top: 377px; color: var(--navy); line-height: 1; white-space: nowrap; }
  .callout .small { font-size: 33px; font-weight: 600; }
  .callout .big { font-size: 52px; font-weight: 700; margin-top: 4px; }

  .portrait { top: 480px; width: 141px; height: 141px; border-radius: 12px; border: 4px solid var(--lime); outline: 3px solid var(--navy); background: linear-gradient(160deg, #b89a72, #c9ab84 50%, #59b6dc); }
  .portrait--left { left: 15px; }
  .portrait--right { left: 756px; background: linear-gradient(180deg, #7fb5e0, #2c72b8 60%, #1e3f73); }
  .agent { font-size: 19px; line-height: 28px; white-space: nowrap; }
  .agent .name { color: var(--red); font-weight: 700; }
  .agent .unit { color: var(--navy); font-weight: 700; letter-spacing: 3px; }
  .agent--left { left: 176px; top: 494px; }
  .agent--right { right: 188px; top: 490px; text-align: right; }
  .divider { left: 480px; top: 495px; width: 2px; height: 120px; background: linear-gradient(180deg, transparent, #cfcfcf 30%, #cfcfcf 70%, transparent); }
  .footer-url { left: 0; right: 0; bottom: 0; height: 25px; background: var(--navy); color: var(--white); text-align: center; font-size: 16px; letter-spacing: 7px; line-height: 25px; }

  .back-title { left: 31px; top: 28px; font-size: 40px; font-weight: 600; color: var(--navy); line-height: 1; white-space: nowrap; }
  .back-address { left: 31px; top: 74px; font-size: 20px; font-weight: 600; color: var(--lime-text); letter-spacing: .5px; white-space: nowrap; }
  .back-copy { left: 31px; top: 106px; font-size: 19px; line-height: 23px; white-space: nowrap; }
  .visit { left: 31px; top: 396px; font-size: 16px; }
  .visit .label { font-family: 'Oswald', sans-serif; font-size: 19px; font-weight: 500; color: var(--navy); display: block; line-height: 22px; }
  .back-agent { top: 464px; font-size: 17px; line-height: 28px; color: var(--navy); white-space: nowrap; }
  .back-agent .name { font-weight: 700; }
  .back-agent--left { left: 28px; }
  .back-agent--right { left: 255px; }
  .stamp { left: 794px; top: 23px; width: 106px; height: 125px; background: var(--stamp); }
</style>
</head>
<body>
<div class="stage">

  <section class="card card--front">
    <svg class="card-art" viewBox="0 0 927 660">
      <defs>
        <linearGradient id="homeTones" x1="0" y1="0" x2="0" y2="1">
          <stop offset="0" stop-color="#7fa9e2"/>
          <stop offset=".35" stop-color="#c7c4e0"/>
          <stop offset=".55" stop-color="#7e8794"/>
          <stop offset=".72" stop-color="#4f7d32"/>
          <stop offset="1" stop-color="#2d5a1c"/>
        </linearGradient>
      </defs>
      <rect x="0" y="0" width="927" height="12" fill="var(--rule)"/>
      <rect x="400" y="373" width="527" height="100" fill="var(--lime)"/>
      <path d="M0 0 H362 C425 90 440 330 400 473 H0 Z" fill="url(#homeTones)" role="img" aria-label="Photo of a large two-storey family home at dusk with a green lawn"/>
      <path d="M378 0 C441 90 456 330 416 473" fill="none" stroke="var(--lime)" stroke-width="6"/>
      <path d="M362 0 C425 90 440 330 400 473" fill="none" stroke="var(--navy)" stroke-width="9"/>
      <path d="M0 0 H360 C335 60 295 100 230 105 H0 Z" fill="var(--navy)"/>
    </svg>
    <div class="abs brand-mark brand-mark--front"><span class="square"></span>Listing Network</div>
    <h1 class="abs display headline">Just Sold!</h1>
    <h2 class="abs display agency-title">Harborline Realty</h2>
    <p class="abs listing listing--one">80 Play: Axul in Quilting 8 1 bedrooms. 2 bathroom<br>985 sq ft Sold fat $769,000 all" side</p>
    <p class="abs listing listing--two">70 Play: Axul in Quilting 8 1 bedrooms. 2 bathroom<br>985 sq ft Sold fat $769,000 all" side</p>
    <div class="abs display callout">
      <div class="small">Were local agents and your</div>
      <div class="big">Neighbors call us!</div>
    </div>
    <div class="abs portrait portrait--left" role="img" aria-label="Portrait photo of agent Marla Denton"></div>
    <div class="abs agent agent--left">
      <div class="name">MARLA DENTON</div>
      <div>(555) 214 7380</div>
      <div>Marla@harborline.test</div>
      <div class="unit">UNIT 4-12</div>
    </div>
    <div class="abs divider"></div>
    <div class="abs agent agent--right">
      <div class="name">THEO VARGA</div>
      <div>(555) 608-1192</div>
      <div>Theo@harborline.test</div>
      <div class="unit">UNIT 6-31</div>
    </div>
    <div class="abs portrait portrait--right" role="img" aria-label="Portrait photo of agent Theo Varga by the sea"></div>
    <div class="abs footer-url">www.HarborlineRealty.test</div>
  </section>

  <section class="card card--back">
    <svg class="card-art" viewBox="0 0 927 662">
      <defs>
        <linearGradient id="roomTones" x1="0" y1="0" x2="1" y2="1">
          <stop offset="0" stop-color="#8a5a2e"/>
          <stop offset=".45" stop-color="#c9b08c"/>
          <stop offset=".75" stop-color="#b5763a"/>
          <stop offset="1" stop-color="#5a3a22"/>
        </linearGradient>
      </defs>
      <path d="M0 211 H451 C462 270 467 330 466 384 H0 Z" fill="url(#roomTones)" role="img" aria-label="Photo of a modern living room with a beige sectional sofa and orange cushions"/>
      <path d="M0 452 H455 C448 490 440 525 425 555 H0 Z" fill="var(--lime)"/>
      <path d="M378 0 C508 200 508 400 443 555" fill="none" stroke="var(--lime)" stroke-width="5"/>
      <path d="M360 0 C490 200 490 400 425 555" fill="none" stroke="var(--navy)" stroke-width="11"/>
    </svg>
    <h2 class="abs display back-title">Harborline Realty</h2>
    <p class="abs display back-address">214 Crescent Ave Seabrook, CA 00000</p>
    <p class="abs back-copy">We are Seabrook agents and your<br>Lantern Bay neighbors.<br>Call us for a tree property market<br>evaluation.</p>
    <p class="abs visit"><span class="label">Visit Us At</span>www.HarborlineRealty.test</p>
    <div class="abs back-agent back-agent--left">
      <div class="name">MARLA DENTON</div>
      <div>(555) 214-7380</div>
      <div>Marla@harborline.test</div>
    </div>
    <div class="abs back-agent back-agent--right">
      <div class="name">THEO VARGA</div>
      <div>(555) 608-1192</div>
      <div>Theo@harborline.test</div>
    </div>
    <div class="abs brand-mark brand-mark--back"><span class="square"></span>Listing Network</div>
    <div class="abs stamp" role="img" aria-label="Postage stamp area"></div>
  </section>

</div>
</body>
</html>
```